Recruitment of Brindle Staffing for the UK market

I want a website for the UK market to attract businesses and companies to come to us for Philipine labour. We want an information site that gives all information on what we do and how we can recruit Philippine labour.
This is a recruitment site for companies to contact us with their requirements for skilled workers coming from the Philipines over to the UK to work.

Target Market(s)

Uk Companies and businesses who want Philipine skilled workers

Industry/Entity Type

REcruitment

Coding

Coded - Design and coding required

Number of Pages Required

5+ page

Font styles to use
Sans Serif

Colors
0054AA
0677BA
7BADD7
CADEEF
E8F1F8
0094D4
00A9DD
6FCCEA
C7EBF8
E9F6FB
EE7325
F08F49
F5BC92
FAE3D3
FDF4ED
EB3D1F
EC4F4E
F09395
F8D3D4
FCEDEE

Requirements
Must have
• Look professional and corperate with drop down menus for Home ,about, services,articles. training , contact us
Nice to have
• Look at Tovel recruitment- https://tovelrecruitment.example.co.uk/. This is my current site - https://www.brindlestaffing.example.com/
Should not have
• Cartoons or silly pictures , needs to be corperate looking

```html
<!DOCTYPE html>
<html lang="en">
<head>
<meta charset="utf-8">
<title>Brindle Staffing – Skilled Philippine Workers for UK Companies</title>
<link href="https://fonts.googleapis.com/css2?family=Barlow:wght@400;500;600;700&display=swap" rel="stylesheet">
<style>
:root{
  --blue:#0054AA;
  --blue-mid:#0677BA;
  --blue-light:#7BADD7;
  --blue-pale:#CADEEF;
  --blue-mist:#E8F1F8;
  --cyan:#0094D4;
  --cyan-bright:#00A9DD;
  --orange:#EE7325;
  --red:#EB3D1F;
  --ink:#1c1c1c;
  --text:#4a4a4a;
  --grey-bg:#f4f4f4;
  --dark:#262626;
  --white:#ffffff;
}
*{margin:0;padding:0;box-sizing:border-box}
html,body{width:1200px;height:4228px;overflow:hidden}
body{font-family:'Barlow',Arial,sans-serif;color:var(--ink);background:var(--white);position:relative}
.abs{position:absolute}
.photo{position:absolute}
.eyebrow{font-size:15px;letter-spacing:2.5px;color:var(--blue);font-weight:500;text-transform:uppercase;display:flex;align-items:center;gap:10px}
.eyebrow .rule{display:inline-block;width:64px;height:2px;background:var(--blue);position:relative}
.eyebrow .rule::before{content:"";position:absolute;left:0;top:-2px;width:6px;height:6px;border-radius:50%;background:var(--blue)}
.heading{font-weight:600;font-size:30px;line-height:34px;letter-spacing:1.2px;text-transform:uppercase;color:var(--ink)}
.body-text{font-size:15.5px;line-height:27px;color:var(--text)}
.btn-outline{position:absolute;display:flex;align-items:center;justify-content:center;border:2px solid var(--blue);color:var(--blue);font-weight:600;font-size:13.5px;letter-spacing:1.2px;background:var(--white)}

/* header */
.site-header{position:absolute;left:0;top:0;width:1200px;height:75px;background:var(--white)}
.brand{position:absolute;left:118px;top:22px;display:flex;align-items:center;gap:10px;font-weight:700;font-size:24px;color:var(--red)}
.brand .mark{width:22px;height:22px;background:var(--red)}
.main-nav{position:absolute;top:32px;font-size:12.5px;font-weight:500;letter-spacing:.6px;color:#333}
.main-nav span{position:absolute;white-space:nowrap;display:flex;align-items:center;gap:5px}
.main-nav .active{color:var(--blue)}
.main-nav .active::after{content:"";position:absolute;left:0;right:0;top:20px;height:2px;background:var(--blue)}
.phone-box{position:absolute;left:977px;top:0;width:223px;height:75px;background:var(--blue);color:var(--white);display:flex;align-items:center;justify-content:center;gap:10px;font-size:17px}

/* hero */
.hero{position:absolute;left:0;top:75px;width:1200px;height:780px;background:linear-gradient(180deg,#e9eef3 0%,#f2f5f8 60%,#fff 72%)}
.hero-eyebrow{position:absolute;top:47px;width:100%;text-align:center;font-size:17px;letter-spacing:3px;color:#9aa3ab}
.hero-title{position:absolute;top:76px;width:100%;text-align:center;font-weight:600;font-size:31px;line-height:41px;letter-spacing:1px}
.hero-title .accent{color:var(--red)}
.scroll-cue{position:absolute;left:18px;top:230px;font-size:10px;letter-spacing:3px;color:#666;transform:rotate(-90deg);transform-origin:left top;white-space:nowrap}
.scroll-line{position:absolute;left:29px;top:360px;width:2px;height:40px;background:var(--blue)}
.feature-card{position:absolute;color:var(--white);text-align:center;display:flex;flex-direction:column;align-items:center}
.feature-card h3{font-weight:600;font-size:19px;letter-spacing:1px;margin-top:12px}
.feature-card p{font-size:11.5px;line-height:19px;margin-top:12px;opacity:.9;padding:0 40px}
.feature-card .btn{margin-top:14px;border:2px solid var(--white);padding:8px 22px;font-size:11px;font-weight:600;letter-spacing:.6px}

/* about */
.frame-blue{position:absolute;background:var(--blue)}
.frame-outline{position:absolute;border:2px solid var(--blue)}

/* team */
.team{position:absolute;left:0;top:1461px;width:1200px;height:661px;background:var(--grey-bg)}
.team-card{position:absolute;background:var(--white);padding:26px 22px 0 28px;box-shadow:0 4px 14px rgba(0,0,0,.06)}
.team-card h4{font-weight:600;font-size:17px;letter-spacing:.8px;border-left:3px solid var(--blue);padding-left:10px;margin-left:-14px}
.team-card p{font-size:11.5px;line-height:19.5px;color:#666;margin-top:12px}
.team-card .more{display:inline-block;margin-top:12px;font-size:11px;font-weight:600;color:var(--blue);text-decoration:underline}
.team-card.orange{background:var(--orange);color:var(--white)}
.team-card.orange h4{border-color:var(--white)}
.team-card.orange p,.team-card.orange .more{color:var(--white)}

/* workers */
.workers{position:absolute;left:0;top:2124px;width:1200px;height:580px;background:linear-gradient(100deg,#0a4aa0 0%,var(--blue) 40%,var(--blue-mid) 70%);overflow:hidden}
.workers .eyebrow{color:var(--white)}
.workers .eyebrow .rule,.workers .eyebrow .rule::before{background:var(--white)}

/* contact */
.contact{position:absolute;left:0;top:3324px;width:1200px;height:545px;background:linear-gradient(180deg,#dfe8f0 0%,#e9eff5 50%,#dde6ee 100%)}
.field{position:absolute;background:var(--white);border:1px solid #c9d2da;font-size:13.5px;color:#666;padding:0 20px;display:flex;align-items:center}
.field.area{align-items:flex-start;padding-top:20px}
.send{position:absolute;left:506px;top:381px;width:195px;height:46px;background:linear-gradient(90deg,var(--blue-mid),var(--cyan-bright));color:var(--white);display:flex;align-items:center;justify-content:center;font-weight:600;font-size:14px;letter-spacing:1.5px}

/* footer */
.site-footer{position:absolute;left:0;top:3869px;width:1200px;height:359px;background:var(--white)}
.footer-col{position:absolute;top:0;height:194px;border-left:1px solid #e2e2e2}
.footer-col h5{position:absolute;top:60px;font-size:13px;font-weight:600;letter-spacing:.8px;border-left:3px solid var(--blue);padding-left:12px;left:-1px;white-space:nowrap}
.footer-col ul{list-style:none;position:absolute;top:90px;left:20px;font-size:13px;color:#444;line-height:26px}
.social{position:absolute;top:4006px;display:flex;gap:7px;left:150px}
.social span{width:31px;height:31px;border-radius:50%;background:#7a7a7a}
.contact-line{position:absolute;left:890px;display:flex;gap:12px;font-size:12.5px;color:#333;line-height:18px}
.contact-line .ico{width:30px;height:30px;border-radius:50%;background:var(--blue);flex-shrink:0;display:flex;align-items:center;justify-content:center}
.copyright{position:absolute;left:0;top:4174px;width:1200px;text-align:center;font-size:11.5px;color:#555}
.footer-rule{position:absolute;left:0;top:4153px;width:1200px;height:1px;background:#e2e2e2}
</style>
</head>
<body>

<header class="site-header">
  <div class="brand"><span class="mark"></span>Brindle Staffing</div>
  <nav class="main-nav">
    <span class="active" style="left:427px">ABOUT</span>
    <span style="left:512px">SERVICES <svg width="11" height="7" viewBox="0 0 11 7"><path d="M1 1l4.5 4.5L10 1" stroke="#333" fill="none" stroke-width="1.4"/></svg></span>
    <span style="left:619px">ARTICLES</span>
    <span style="left:722px">TRAINING <svg width="11" height="7" viewBox="0 0 11 7"><path d="M1 1l4.5 4.5L10 1" stroke="#333" fill="none" stroke-width="1.4"/></svg></span>
    <span style="left:821px">CONTACT US</span>
  </nav>
  <div class="phone-box">
    <svg width="22" height="22" viewBox="0 0 22 22"><circle cx="11" cy="11" r="11" fill="#fff"/><path d="M7.5 6c.6-.5 1.3-.4 1.7.2l1 1.6c.3.5.2 1.1-.3 1.5l-.6.5c.5 1.2 1.4 2.1 2.6 2.7l.5-.6c.4-.5 1-.6 1.5-.3l1.6 1c.6.4.7 1.1.2 1.7l-.7.8c-.6.6-1.5.8-2.3.4-2.6-1.2-4.6-3.2-5.8-5.8-.4-.8-.2-1.7.4-2.3z" fill="#0054AA"/></svg>
    07700 900123
  </div>
</header>

<section class="hero">
  <div class="hero-eyebrow">BRINDLE STAFFING</div>
  <h1 class="hero-title">RECRUITING AND PLACING SKILLED PHILIPPINE<br><span class="accent">WORKERS INTO UK COMPANIES</span></h1>
  <div class="scroll-cue" style="transform:rotate(-90deg) translate(-100px,0)">SCROLL DOWN</div>
  <div class="scroll-line"></div>
  <div class="photo" role="img" aria-label="Group photo of skilled workers from many professions: engineers, doctors, nurses, builders and office staff" style="left:98px;top:171px;width:1035px;height:397px;background:radial-gradient(ellipse at 50% 60%,#8c99a8 0%,#a9b3bd 45%,rgba(233,238,243,0) 75%)"></div>

  <div class="feature-card" style="left:131px;top:568px;width:307px;height:209px;background:var(--orange);padding-top:30px">
    <svg width="44" height="44" viewBox="0 0 44 44" fill="none" stroke="#fff" stroke-width="1.6"><circle cx="22" cy="13" r="7"/><path d="M12 28c2-5 6-7 10-7s8 2 10 7"/><path d="M6 34c5 0 8 4 14 4h12l6-6"/></svg>
    <h3>HOW WE HELP</h3>
    <p>We work with companies to find skilled workers that meet the UK requirements</p>
  </div>
  <div class="feature-card" style="left:438px;top:541px;width:314px;height:236px;background:var(--blue);padding-top:36px">
    <svg width="42" height="40" viewBox="0 0 42 40" fill="none" stroke="#fff" stroke-width="1.6"><rect x="8" y="3" width="28" height="22"/><path d="M14 10h16M14 15h12"/><circle cx="10" cy="28" r="4"/><path d="M3 39c1-5 4-7 7-7s6 2 7 7"/></svg>
    <h3>OUR TRAINING</h3>
    <p>We need to know what your issues are and how we can understand the personnal you require</p>
    <div class="btn">LEARN MORE</div>
  </div>
  <div class="feature-card" style="left:752px;top:568px;width:313px;height:209px;background:var(--dark);padding-top:28px">
    <svg width="42" height="42" viewBox="0 0 42 42" fill="none" stroke="#fff" stroke-width="1.6"><rect x="5" y="8" width="26" height="30"/><path d="M10 16h14M10 22h14M10 28h9"/><path d="M26 30L38 6l3 2-12 24z"/></svg>
    <h3>CONTACT US TODAY</h3>
    <p>Please contact us today with your requirements , this can be care workers</p>
  </div>
</section>

<section class="about">
  <div class="frame-blue" style="left:120px;top:941px;width:196px;height:20px"></div>
  <div class="frame-blue" style="left:120px;top:941px;width:18px;height:190px"></div>
  <div class="frame-outline" style="left:230px;top:1046px;width:336px;height:275px"></div>
  <div class="photo" role="img" aria-label="Two engineers in hard hats and hi-vis jackets reviewing plans on a factory floor" style="left:141px;top:960px;width:365px;height:314px;background:linear-gradient(135deg,#5a7590,#c9c46a 60%,#7d8a92)"></div>
  <div class="photo" role="img" aria-label="Smiling businessman with glasses writing notes at a meeting table" style="left:379px;top:1165px;width:271px;height:227px;background:linear-gradient(135deg,#8c9196,#c7c9cb 55%,#6f767c)"></div>
  <div class="abs eyebrow" style="left:699px;top:1009px">WHO WE ARE <span class="rule"></span></div>
  <h2 class="abs heading" style="left:699px;top:1034px">WHAT THE<br>BUSINESS IS ABOUT</h2>
  <p class="abs body-text" style="left:699px;top:1118px;width:420px">We source skilled workers directly from the Philippines to work in the UK. With offices , training locations and specialist recruiters we can find the highest quality individuals to add value and resources to any UK business. We delivery quality based on vast experience over a number of years.</p>
  <div class="btn-outline" style="left:699px;top:1282px;width:150px;height:44px">LEARN MORE</div>
</section>

<section class="team">
  <div class="abs eyebrow" style="left:130px;top:67px">WORKING TOGETHER <span class="rule"></span></div>
  <h2 class="abs heading" style="left:130px;top:98px">WE RECRUIT THE FINEST TALENT AVAILABLE<br>WITH OUR DEDICATED 200 STRONG TEAM</h2>
  <div class="photo" role="img" aria-label="Team of medical professionals in white coats and scrubs" style="left:126px;top:213px;width:301px;height:225px;background:linear-gradient(180deg,#d8dde2,#f0f1f2 55%,#6f88a6)"></div>
  <div class="photo" role="img" aria-label="Construction and warehouse workers in hard hats and hi-vis vests" style="left:447px;top:213px;width:300px;height:225px;background:linear-gradient(180deg,#a89a73,#d9c24a 55%,#5f6a74)"></div>
  <div class="photo" role="img" aria-label="Digital figure made of network lines held above a hand on a blue background" style="left:770px;top:213px;width:302px;height:225px;background:radial-gradient(circle at 50% 55%,#5fa4d8,#1d5b9a 55%,#0d3a72)"></div>
  <div class="team-card" style="left:148px;top:389px;width:262px;height:190px">
    <h4>WHAT WE DO</h4>
    <p>Our company has been established in the Philippines for over 20 years. We have mainly been recruiting philippine workers for the off shore industry</p>
    <span class="more">LEARN MORE</span>
  </div>
  <div class="team-card orange" style="left:468px;top:389px;width:262px;height:190px">
    <h4>HOW WE HELP</h4>
    <p>We work with companies to find skilled workers that meet the UK requirements for Visas and work permits. We guide you through the whole process</p>
    <span class="more">LEARN MORE</span>
  </div>
  <div class="team-card" style="left:791px;top:389px;width:263px;height:190px">
    <h4>WHERE TO START</h4>
    <p>We need to know what your issues are and how we can understand the personnal you require . over what time frame and the number of employees you need.</p>
    <span class="more">LEARN MORE</span>
  </div>
</section>

<section class="workers">
  <svg class="abs" style="left:0;top:0" width="1200" height="580" viewBox="0 0 1200 580" role="img" aria-label="Three industrial workers in hard hats standing with arms crossed in a factory">
    <defs><linearGradient id="wk" x1="0" y1="0" x2="1" y2="0"><stop offset="0" stop-color="#4d5358"/><stop offset=".6" stop-color="#8b8f93"/><stop offset="1" stop-color="#b9bcbf"/></linearGradient></defs>
    <polygon points="755,0 1200,0 1200,580 583,580" fill="url(#wk)"/>
  </svg>
  <div class="abs eyebrow" style="left:135px;top:122px">ABOUT WORKERS <span class="rule"></span></div>
  <h2 class="abs heading" style="left:135px;top:148px;color:var(--white)">UK SKILLED WORKERS LIST</h2>
  <p class="abs body-text" style="left:135px;top:196px;width:432px;color:var(--white)">The UK government since brexit have developed a new system based on points (similar to Australia) when recruiting from outside of the UK. Previuosly EU citizens could work in the UK without any extensive documentation or clarification of skills. This has all changed. Overseas recruitment must now focus on skills that are currently short in the UK. The list is extensive and is constandly being reviewed.</p>
  <div class="btn-outline" style="left:135px;top:411px;width:151px;height:45px;background:transparent;border-color:var(--white);color:var(--white)">LEARN MORE</div>
</section>

<section class="training">
  <svg class="abs" style="left:96px;top:2775px" width="536" height="470" viewBox="0 0 536 470">
    <polygon points="134,2 402,2 534,235 402,468 134,468 2,235" fill="none" stroke="#7BADD7" stroke-width="1.5"/>
    <polygon points="150,16 388,16 506,235 388,454 150,454 32,235" fill="#b8bfc6" role="img" aria-label="Presenter smiling beside a flip chart during a training session"/>
  </svg>
  <div class="abs eyebrow" style="left:670px;top:2849px">WHO WE ARE <span class="rule"></span></div>
  <h2 class="abs heading" style="left:670px;top:2875px;font-size:36px;line-height:40px">OUR TRAINING</h2>
  <p class="abs body-text" style="left:670px;top:2925px;width:450px;font-size:16px;line-height:29px">We source skilled workers directly from the Philippines to work in the UK. With offices , training locations and specialist recruiters we can find the highest quality individuals to add value and resources to any UK buisness. We delivery quality based on vast experience over a number of years.</p>
  <div class="btn-outline" style="left:666px;top:3099px;width:161px;height:48px;font-size:14.5px">LEARN MORE</div>
  <div class="abs" style="left:596px;top:3303px;width:2px;height:51px;background:#556"></div>
</section>

<section class="contact" role="img" aria-label="Soft blurred photo of a business meeting behind the contact form">
  <div class="abs" style="left:0;top:79px;width:1200px;text-align:center;font-size:15px;letter-spacing:2.5px;color:var(--blue)">GET IN TOUCH</div>
  <h2 class="abs heading" style="left:0;top:97px;width:1200px;text-align:center">CONTACT US TODAY</h2>
  <div class="field" style="left:192px;top:169px;width:269px;height:58px">Name*</div>
  <div class="field" style="left:469px;top:169px;width:270px;height:58px">Email address*</div>
  <div class="field" style="left:747px;top:169px;width:271px;height:58px">Phone*</div>
  <div class="field area" style="left:192px;top:240px;width:826px;height:115px">Message</div>
  <div class="send">SEND MESSAGE</div>
</section>

<footer class="site-footer">
  <div class="brand" style="left:150px;top:66px"><span class="mark"></span>Brindle Staffing</div>
  <div class="footer-col" style="left:453px;width:182px">
    <h5>QUICK LINKS</h5>
    <ul><li>Home</li><li>About Us</li><li>Services</li><li>Training</li></ul>
  </div>
  <div class="footer-col" style="left:635px;width:225px">
    <h5>RESOURCES</h5>
    <ul><li>Why Us?</li><li>Faq</li><li>Blogs</li><li>Privacy Policy</li></ul>
  </div>
  <div class="footer-col" style="left:860px;width:340px">
    <h5>CONTACT US</h5>
  </div>
</footer>
<div class="social" aria-label="Social media links"><span></span><span></span><span></span><span></span></div>
<div class="contact-line" style="top:3956px">
  <span class="ico"><svg width="14" height="18" viewBox="0 0 14 18"><path d="M7 1a6 6 0 0 1 6 6c0 4.5-6 10-6 10S1 11.5 1 7a6 6 0 0 1 6-6z" fill="#fff"/><circle cx="7" cy="7" r="2.3" fill="#0054AA"/></svg></span>
  <span>123 Lorem Ipsum Address line<br>tempor incididunt ut la</span>
</div>
<div class="contact-line" style="top:4013px;align-items:center;font-weight:600">
  <span class="ico"><svg width="14" height="14" viewBox="0 0 14 14"><path d="M2.5 1c.6-.5 1.3-.4 1.7.2l1 1.6c.3.5.2 1.1-.3 1.5l-.6.5c.5 1.2 1.4 2.1 2.6 2.7l.5-.6c.4-.5 1-.6 1.5-.3l1.6 1c.6.4.7 1.1.2 1.7l-.7.8c-.6.6-1.5.8-2.3.4C5.1 9.3 3.1 7.3 1.9 4.7c-.4-.8-.2-1.7.4-2.3z" fill="#fff"/></svg></span>
  <span>(555) 010-4477</span>
</div>
<div class="contact-line" style="top:4067px;align-items:center;font-weight:600">
  <span class="ico"><svg width="15" height="11" viewBox="0 0 15 11"><rect x=".5" y=".5" width="14" height="10" fill="#fff"/><path d="M.5.5l7 5.5 7-5.5" stroke="#0054AA" fill="none"/></svg></span>
  <span>hello@brindlestaffing.example.com</span>
</div>
<div class="footer-rule"></div>
<div class="copyright">© 2023 All Rights Reserved | Brindle Staffing Ltd</div>

</body>
</html>
```